Yoga for Scoliosis business card/logo design

I need a business card/logo design for my new business. I am a registered yoga teacher and am certified in yoga for scoliosis. I'd like my card to read "Marlow Yoga Yoga for a Healthy Spine" and would like to incorporate one of the letters in my name{ ie the first vertical line of the letter " H "or "D"} to resemble a scoliotic spine. I regularly teach the following:Yoga for Scoliosis, Yoga for Back Health, Hatha yoga, Vinyasa yoga with Iyengar style alignment. This business is mostly for private clients, but I also teach group, semi-private & work shop classes. I like the colors green (light emerald) and royal blue. I'd like the design to be somewhat sleek, but not too modern. I also like the idea of a ying/yang symbol with a scoliotic spine dviding it.

Danielle Marlow
200 RYT, Certified Yoga for Scoliosis Instructor
MarlowYoga.example
MarlowYoga@mailbox.example
555-412-3097

```html
<!DOCTYPE html>
<html lang="en">
<head>
<meta charset="utf-8">
<title>Marlow Yoga – Business Card</title>
<link rel="stylesheet" href="https://fonts.googleapis.com/css2?family=Open+Sans:wght@400;700&display=swap">
<style>
  :root {
    --backdrop: #3a1515;
    --card: #ffffff;
    --royal: #1f2a7a;
    --emerald: #35b98c;
    --emerald-deep: #1f9e78;
  }
  html, body {
    margin: 0;
    width: 1200px;
    height: 800px;
    overflow: hidden;
    background: var(--backdrop);
    font-family: "Open Sans", Arial, sans-serif;
  }
  .card {
    position: absolute;
    left: 180px;
    top: 160px;
    width: 840px;
    height: 480px;
    background: var(--card);
    box-shadow: 0 12px 40px rgba(0,0,0,.45);
    text-align: center;
    color: var(--royal);
  }
  .band {
    position: absolute;
    left: 0;
    width: 100%;
    height: 6px;
    background: var(--emerald);
  }
  .band--upper { top: 140px; }
  .band--lower { top: 412px; }
  .brand-mark {
    position: absolute;
    left: 375px;
    top: 28px;
    width: 90px;
    height: 90px;
    border-radius: 50%;
    background: var(--emerald);
  }
  .brand-name {
    position: absolute;
    top: 146px;
    left: 0;
    width: 100%;
    margin: 0;
    font-size: 54px;
    font-weight: 400;
    line-height: 1;
    color: var(--royal);
  }
  .brand-tagline {
    position: absolute;
    top: 206px;
    left: 0;
    width: 100%;
    margin: 0;
    font-size: 16px;
    letter-spacing: 6px;
    color: var(--emerald-deep);
  }
  .contact {
    position: absolute;
    top: 238px;
    left: 0;
    width: 100%;
  }
  .contact p { margin: 0; }
  .contact__name {
    font-size: 26px;
    font-weight: 700;
    color: var(--emerald-deep);
    line-height: 1.2;
  }
  .contact__credential {
    font-size: 16px;
    line-height: 1.4;
  }
  .contact__phone {
    margin-top: 8px !important;
    font-size: 26px;
    line-height: 1.3;
  }
  .contact__web,
  .contact__email {
    font-size: 19px;
    line-height: 1.45;
  }
</style>
</head>
<body>
  <div class="card">
    <div class="brand-mark"></div>
    <div class="band band--upper"></div>
    <h1 class="brand-name">Marlow Yoga</h1>
    <p class="brand-tagline">Yoga for a Healthy Spine</p>
    <div class="contact">
      <p class="contact__name">Danielle Marlow</p>
      <p class="contact__credential">200 RYT, Certified Yoga for Scoliosis Instructor</p>
      <p class="contact__phone">555-412-3097</p>
      <p class="contact__web">MarlowYoga.example</p>
      <p class="contact__email">MarlowYoga@mailbox.example</p>
    </div>
    <div class="band band--lower"></div>
  </div>
</body>
</html>
```